KTR Builders
Home Page
Project: KTR Builders
KTR Builders  -
Creative Brief
www.ktrbuilders.com
KTR Builders is a residential general contractor. We build new custom homes, house additions, bathroom and kitchen remodeling.
We also can do medium size commercial buildings and office space buildout.
KTR Builders is also trained installer of the Brindell Pools.
We Need template of the home page and design of the sub pages.
yellow
Verdana, Trebuchet MS, Georgia

```html
<!DOCTYPE html>
<html lang="en">
<head>
<meta charset="utf-8">
<title>KTR Builders — Home</title>
<link rel="stylesheet" href="https://fonts.googleapis.com/css2?family=Arimo:wght@400;700&display=swap">
<style>
  :root {
    --page-bg: #5b636b;
    --panel-dark: #3d444c;
    --tile: #6c757e;
    --tile-line: #858e97;
    --tile-active: #434a52;
    --brand-blue: #2b8fe0;
    --brand-blue-dark: #1467bf;
    --accent: #4fb3ff;
    --text-light: #ffffff;
    --text-muted: #aab3bc;
    --link: #ffffff;
    --rule: #5a626b;
  }
  * { box-sizing: border-box; margin: 0; padding: 0; }
  html, body { width: 1200px; height: 1096px; overflow: hidden; }
  body {
    background: var(--page-bg);
    font-family: "Arimo", Arial, sans-serif;
    color: var(--text-light);
    position: relative;
  }
  .sound-toggle {
    position: absolute; right: 42px; top: 104px;
    font-size: 15px; color: var(--text-muted);
  }
  .sound-toggle b { color: var(--text-light); font-weight: 400; }

  .site {
    position: absolute; left: 148px; top: 140px;
    width: 1010px; height: 894px;
  }
  .brand-tile {
    position: absolute; left: 0; top: 0; width: 371px; height: 321px;
    background: radial-gradient(circle at 40% 40%, #55b3ff 0%, var(--brand-blue) 45%, var(--brand-blue-dark) 100%);
    display: flex; flex-direction: column; align-items: center; justify-content: center; gap: 22px;
  }
  .brand-mark { width: 70px; height: 70px; background: var(--text-light); }
  .brand-name {
    font-size: 34px; font-weight: 700; color: var(--text-light); letter-spacing: 1px;
  }

  .main-nav {
    position: absolute; left: 371px; top: 0; width: 639px; height: 321px;
    display: grid; grid-template-columns: repeat(3, 1fr); grid-template-rows: repeat(2, 1fr);
    gap: 3px; background: var(--page-bg); padding-left: 3px;
  }
  .nav-tile {
    position: relative; background: var(--tile);
    border: 1px solid var(--tile-line);
    display: flex; align-items: center; justify-content: center;
    font-size: 19px; text-transform: uppercase; color: var(--text-light);
    text-decoration: none;
  }
  .nav-tile.is-active { background: var(--tile-active); border-color: var(--tile-line); font-weight: 700; }
  .nav-tile.is-active span { border-bottom: 2px solid var(--text-light); padding-bottom: 4px; }
  .nav-tile svg { position: absolute; right: 10px; bottom: 10px; }

  .hero-photo {
    position: absolute; left: 0; top: 321px; width: 371px; height: 573px;
    background: linear-gradient(160deg, #1b6fd0 0%, #4aa0ee 40%, #9fd0f7 65%, #2f6f8e 100%);
  }

  .content {
    position: absolute; left: 371px; top: 321px; width: 639px; height: 573px;
    background: var(--panel-dark);
    border-left: 3px solid var(--page-bg); border-top: 3px solid var(--page-bg);
  }
  .section-title { font-size: 19px; text-transform: uppercase; color: var(--text-light); }
  .section-title em { font-style: normal; color: var(--accent); font-weight: 700; }
  .welcome-title { position: absolute; left: 53px; top: 46px; }
  .welcome-photo {
    position: absolute; left: 53px; top: 80px; width: 154px; height: 132px;
    background: linear-gradient(180deg, #cfd8e2 0%, #8ea4bb 55%, #3c5878 100%);
    border: 2px solid #c9d0d7;
  }
  .welcome-text { position: absolute; left: 238px; top: 86px; width: 360px; font-size: 14.5px; line-height: 19px; }
  .welcome-text strong { display: block; color: var(--text-light); margin-bottom: 14px; }
  .welcome-text p { color: var(--text-muted); }
  .divider { position: absolute; left: 53px; top: 240px; width: 535px; border-top: 1px solid var(--rule); }

  .services { position: absolute; left: 53px; top: 264px; width: 230px; }
  .news { position: absolute; left: 303px; top: 264px; width: 260px; }
  .col-rule { position: absolute; left: 278px; top: 262px; height: 228px; border-left: 1px solid var(--rule); }
  .service-list { list-style: none; margin-top: 30px; }
  .service-list li { font-size: 14.5px; line-height: 26px; padding-left: 16px; position: relative; }
  .service-list li::before { content: ""; position: absolute; left: 0; top: 12px; width: 4px; height: 4px; background: var(--text-light); }
  .service-list a { color: var(--link); }
  .more-link { position: absolute; left: 155px; top: 477px; font-size: 13px; color: var(--text-light); font-weight: 700; }
  .more-link::before { content: "› "; }
  .news-item { margin-top: 30px; font-size: 14px; line-height: 18px; }
  .news-item + .news-item { margin-top: 18px; }
  .news-date { color: var(--accent); font-weight: 700; display: block; margin-bottom: 5px; }
  .news-item p { color: var(--text-muted); }

  .site-footer {
    position: absolute; left: 0; bottom: 14px; width: 430px;
    font-size: 12px; color: var(--text-muted); text-align: center;
  }
  .site-footer a { color: var(--text-muted); }
</style>
</head>
<body>
  <div class="sound-toggle">sound <b>on</b>/off</div>

  <div class="site">
    <header class="brand-tile">
      <div class="brand-mark"></div>
      <div class="brand-name">KTR BUILDERS INC.</div>
    </header>

    <nav class="main-nav">
      <a class="nav-tile is-active" href="#"><span>Home</span></a>
      <a class="nav-tile" href="#">About us<svg width="10" height="10" viewBox="0 0 10 10"><path d="M1 1 L9 9 M9 3 V9 H3" stroke="#c9d0d7" fill="none" stroke-width="1.5"/></svg></a>
      <a class="nav-tile" href="#">Services<svg width="10" height="10" viewBox="0 0 10 10"><path d="M1 1 L9 9 M9 3 V9 H3" stroke="#c9d0d7" fill="none" stroke-width="1.5"/></svg></a>
      <a class="nav-tile" href="#">Prices<svg width="10" height="10" viewBox="0 0 10 10"><path d="M1 1 L9 9 M9 3 V9 H3" stroke="#c9d0d7" fill="none" stroke-width="1.5"/></svg></a>
      <a class="nav-tile" href="#">Projects<svg width="10" height="10" viewBox="0 0 10 10"><path d="M1 1 L9 9 M9 3 V9 H3" stroke="#c9d0d7" fill="none" stroke-width="1.5"/></svg></a>
      <a class="nav-tile" href="#">Contact us<svg width="10" height="10" viewBox="0 0 10 10"><path d="M1 1 L9 9 M9 3 V9 H3" stroke="#c9d0d7" fill="none" stroke-width="1.5"/></svg></a>
    </nav>

    <div class="hero-photo" role="img" aria-label="Glass office tower against a blue sky"></div>

    <main class="content">
      <h1 class="section-title welcome-title"><em>Welcome</em> to our website!</h1>
      <div class="welcome-photo" role="img" aria-label="Builder in a hard hat in front of a new building"></div>
      <div class="welcome-text">
        <strong>Lorem ipsum dolor sit amet, consectetuer adipiscing elit, sed</strong>
        <p>Diam nonummy nibh euismod tincidunt ut laoreet dolore magna aliquam erat volutpat.</p>
      </div>
      <div class="divider"></div>

      <section class="services">
        <h2 class="section-title"><em>Our</em> services</h2>
        <ul class="service-list">
          <li><a href="#">Lorem ipsum dolor sit</a></li>
          <li><a href="#">Consectetuer adipiscing</a></li>
          <li><a href="#">Sed diam nonummy nibh</a></li>
          <li><a href="#">Euismod tincidunt ut la</a></li>
          <li><a href="#">Dolore magna aliquam</a></li>
        </ul>
      </section>
      <div class="col-rule"></div>
      <section class="news">
        <h2 class="section-title"><em>News &amp;</em> events</h2>
        <div class="news-item">
          <span class="news-date">[ 10.10.11 ]</span>
          <p>Lorem ipsum dolor sit amet, consectetuer adipiscing elit, sed diam nonummy nibh</p>
        </div>
        <div class="news-item">
          <span class="news-date">[ 10.10.11 ]</span>
          <p>Lorem ipsum dolor sit amet, consectetuer adipiscing elit, sed diam nonummy nibh</p>
        </div>
      </section>
      <a class="more-link" href="#">more services</a>

      <footer class="site-footer">KTR BUILDERS 2011 <a href="#">Privacy policy</a> | <a href="#">Terms of use</a></footer>
    </main>
  </div>
</body>
</html>
```